We need a single web page design for a promotion. This page will acts as a landing page for users. Please provide us with a cutting edge design. I have attached a previous design used a couple of years ago.

Link: http://www.brightleafsnaps.com/bonuspack/
Updates

The Start Here box needs to look like this:

-Start Here (heading) 
-A box for email addresses to be entered
-Then a check box with "Yes, I have read and agree to the Privacy Policy and agree to receive email marketing from Bright Leaf Snaps and acknowledge that I will receive special email offers from our marketing partners, including the Ledger Post newsletter."
-A submit button 

All of this information needs to be in one box please.  And please feel free to contact me if you have any questions about this. 

Target Market(s)

Middle aged women (housewives)

Requirements
Must have
• Images must reflect the "500 Photo Prints". The only fields that are necessary are a box for email and a submit button.
Should not have
• The word FREE anywhere on the page

```html
<!DOCTYPE html>
<html lang="en">
<head>
<meta charset="utf-8">
<title>Bright Leaf Snaps – 500 Photo Prints</title>
<link rel="stylesheet" href="https://fonts.googleapis.com/css2?family=Exo+2:ital,wght@0,700;1,800;1,900&family=Open+Sans:wght@400;700&display=swap">
<style>
  :root {
    --sky: #3fb4d3;
    --sky-deep: #2a9cbd;
    --sky-light: #6fcbe2;
    --ink-top: #0e2a33;
    --footer: #0b1d24;
    --footer-text: #d6e3e7;
    --navy: #0d2a3a;
    --field: #1ea3c6;
    --field-dark: #138cae;
    --lime: #a6d62a;
    --lime-light: #c9ee5a;
    --lime-dark: #7fae12;
    --white: #ffffff;
    --headline-shadow: rgba(20, 70, 90, 0.45);
    --photo-warm: #d9a36c;
    --photo-skin: #e6b48e;
    --photo-hair: #5b3a24;
    --photo-sand: #efe2cf;
    --photo-flower: #f2b521;
  }
  * { box-sizing: border-box; margin: 0; padding: 0; }
  html, body { width: 1200px; height: 695px; overflow: hidden; }
  body { font-family: "Open Sans", Arial, sans-serif; background: var(--sky); }

  .landing {
    position: relative; width: 1200px; height: 695px; overflow: hidden;
    background: radial-gradient(ellipse at 45% 40%, var(--sky-light) 0%, var(--sky) 45%, var(--sky-deep) 100%);
  }
  .top-band { position: absolute; left: 0; top: 0; width: 100%; height: 11px; background: var(--ink-top); }
  .backdrop-pattern {
    position: absolute; left: 0; top: 11px; width: 100%; height: 561px;
    background: linear-gradient(180deg, rgba(255,255,255,0.06), rgba(0,60,90,0.12));
  }

  /* photo stack */
  .photo-stack { position: absolute; left: 120px; top: 40px; width: 480px; height: 440px; }
  .print {
    position: absolute; background: var(--white); padding: 10px;
    box-shadow: 0 4px 10px rgba(0, 40, 60, 0.35);
  }
  .print-fill { width: 100%; height: 100%; }
  .print.back-1 { left: 70px; top: 30px; width: 360px; height: 300px; transform: rotate(12deg); }
  .print.back-1 .print-fill { background: linear-gradient(135deg, var(--photo-flower), #c46b12); }
  .print.back-2 { left: 40px; top: 60px; width: 370px; height: 300px; transform: rotate(-4deg); }
  .print.back-2 .print-fill { background: linear-gradient(135deg, #bfc4c6, #8c8f8e); }
  .print.back-3 { left: 20px; top: 100px; width: 360px; height: 290px; transform: rotate(-14deg); }
  .print.back-3 .print-fill { background: linear-gradient(135deg, var(--photo-flower), #a8612a); }
  .print.front { left: 45px; top: 75px; width: 420px; height: 340px; transform: rotate(-18deg); padding: 12px; }
  .print.front .print-fill {
    background: linear-gradient(110deg, var(--photo-hair) 0%, var(--photo-skin) 35%, var(--photo-warm) 55%, var(--photo-sand) 80%);
  }

  /* headline */
  .headline { position: absolute; left: 640px; top: 40px; width: 440px; height: 260px; color: var(--white); font-family: "Exo 2", Arial, sans-serif; font-style: italic; text-shadow: 2px 3px 4px var(--headline-shadow); }
  .headline span { position: absolute; white-space: nowrap; }
  .headline .get { left: 35px; top: 6px; font-size: 50px; font-weight: 900; }
  .headline .count { left: 118px; top: -30px; font-size: 196px; font-weight: 900; letter-spacing: -8px; line-height: 1; color: #f1f5f6; transform: scaleX(0.88); transform-origin: left center; }
  .headline .prints { left: 16px; top: 164px; font-size: 54px; font-weight: 900; letter-spacing: 0.5px; }
  .headline .delivered { left: 8px; top: 216px; font-size: 33px; font-weight: 800; }

  /* form card */
  .signup-card {
    position: absolute; left: 628px; top: 300px; width: 437px; height: 177px;
    background: linear-gradient(180deg, #ffffff, #eef2f3); border-radius: 3px;
    box-shadow: 0 3px 8px rgba(0, 40, 60, 0.35);
  }
  .rivet { position: absolute; width: 7px; height: 7px; border-radius: 50%; background: var(--field); }
  .rivet.tl { left: 7px; top: 9px; } .rivet.tr { right: 7px; top: 9px; }
  .rivet.bl { left: 7px; bottom: 8px; } .rivet.br { right: 7px; bottom: 8px; }
  .signup-title { position: absolute; left: 22px; top: 8px; font-family: "Exo 2", Arial, sans-serif; font-weight: 900; font-style: italic; font-size: 33px; color: var(--navy); white-space: nowrap; }
  .email-field {
    position: absolute; left: 18px; top: 55px; width: 400px; height: 43px;
    background: linear-gradient(180deg, var(--field), var(--field-dark));
    border: none; color: var(--white); font-family: "Open Sans", Arial, sans-serif; font-size: 17px; padding-left: 10px;
  }
  .email-field::placeholder { color: var(--white); }
  .consent { position: absolute; left: 18px; top: 108px; width: 305px; display: flex; gap: 9px; font-size: 9.2px; line-height: 1.35; color: #444; }
  .consent input { width: 13px; height: 13px; flex: none; margin-top: 1px; }
  .consent strong { color: #222; }
  .submit-button {
    position: absolute; left: 332px; top: 112px; width: 86px; height: 36px;
    background: linear-gradient(180deg, var(--lime-light), var(--lime)); border: 1px solid var(--lime-dark); border-radius: 3px;
    color: var(--white); font-family: "Exo 2", Arial, sans-serif; font-weight: 700; font-size: 18px; text-shadow: 0 1px 2px rgba(60, 90, 0, 0.6);
  }

  /* benefits bar */
  .benefits {
    position: absolute; left: 106px; top: 507px; width: 991px; height: 43px; border-radius: 22px;
    background: linear-gradient(180deg, var(--lime-light), var(--lime) 55%, var(--lime-dark));
    list-style: none;
    box-shadow: 0 2px 5px rgba(0, 40, 60, 0.35);
  }
  .benefit {
    position: absolute; top: 0; height: 43px; display: flex; align-items: center; gap: 7px;
    white-space: nowrap; color: var(--white); font-family: "Exo 2", Arial, sans-serif; font-weight: 700; font-size: 17.5px;
    text-shadow: 0 1px 2px rgba(60, 90, 0, 0.6);
  }
  .benefit.quality { left: 10px; }
  .benefit.storage { left: 368px; }
  .benefit.sharing { left: 622px; }
  .tick { width: 26px; height: 26px; flex: none; }

  /* footer */
  .legal { position: absolute; left: 0; top: 572px; width: 100%; height: 123px; background: var(--footer); color: var(--footer-text); font-size: 9.2px; line-height: 1.42; text-align: center; padding: 14px 138px 0; }
  .legal p + p { margin-top: 11px; }
  .legal a { color: #5fc3e3; }
</style>
</head>
<body>
<main class="landing">
  <div class="top-band"></div>
  <div class="backdrop-pattern" role="img" aria-label="Faint grid of small photo thumbnails"></div>

  <div class="photo-stack">
    <div class="print back-1"><div class="print-fill" role="img" aria-label="Photo print of a yellow flower"></div></div>
    <div class="print back-2"><div class="print-fill" role="img" aria-label="Photo print in soft grey tones"></div></div>
    <div class="print back-3"><div class="print-fill" role="img" aria-label="Photo print of yellow daisies"></div></div>
    <div class="print front"><div class="print-fill" role="img" aria-label="Photo print of a smiling young woman at the beach"></div></div>
  </div>

  <h1 class="headline">
    <span class="get">GET</span>
    <span class="count">500</span>
    <span class="prints">PHOTO PRINTS</span>
    <span class="delivered">DELIVERED TO YOU</span>
  </h1>

  <form class="signup-card" action="http://www.brightleafsnaps.com/bonuspack/">
    <span class="rivet tl"></span><span class="rivet tr"></span><span class="rivet bl"></span><span class="rivet br"></span>
    <h2 class="signup-title">START HERE</h2>
    <input class="email-field" type="email" placeholder="Your E-mail here_">
    <label class="consent"><input type="checkbox"><span>Yes, I have read and agree to the Privacy Policy and agree to receive email marketing from <strong>Bright Leaf Snaps</strong> and acknowledge that I will receive special email offers from our marketing partners, including the Ledger Post newsletter.</span></label>
    <button class="submit-button" type="submit">SUBMIT</button>
  </form>

  <ul class="benefits">
    <li class="benefit quality"><svg class="tick" viewBox="0 0 26 26"><circle cx="13" cy="13" r="12" fill="#eaf7c4" stroke="#7fae12"/><path d="M7 13.5l4 4 8-9" fill="none" stroke="#5f8c0a" stroke-width="3" stroke-linecap="round" stroke-linejoin="round"/></svg>PROFESSIONAL QUALITY PHOTOS</li>
    <li class="benefit storage"><svg class="tick" viewBox="0 0 26 26"><circle cx="13" cy="13" r="12" fill="#eaf7c4" stroke="#7fae12"/><path d="M7 13.5l4 4 8-9" fill="none" stroke="#5f8c0a" stroke-width="3" stroke-linecap="round" stroke-linejoin="round"/></svg>UNLIMITED STORAGE</li>
    <li class="benefit sharing"><svg class="tick" viewBox="0 0 26 26"><circle cx="13" cy="13" r="12" fill="#eaf7c4" stroke="#7fae12"/><path d="M7 13.5l4 4 8-9" fill="none" stroke="#5f8c0a" stroke-width="3" stroke-linecap="round" stroke-linejoin="round"/></svg>SHARE WITH YOUR FAMILY &amp; FRIENDS</li>
  </ul>

  <footer class="legal">
    <p>*OFFER REDEMPTION WILL REQUIRE PARTICIPATION AND / OR PURCHASE OF THIRD PARTY OFFERS.</p>
    <p>To receive the membership incentive gift of Five Hundred (500) photo prints you must complete all of the steps outlined herein. Prospective members must: (a) submit their zip code to determine geographic eligibility; (b) register with a valid and deliverable email address; (c) submit accurate contact and demographic information including a mailing address; (d) Accumulate a total of Twenty Five (25) points by either answering survey questions, completing lead questionnaires, or taking advantage of 3rd party offers. Purchase may be required. Please read participation requirements for details.</p>
    <p>On each page, you will be able to see your current point total and the total number of points necessary to redeem the incentive gift. Upon completion of all requirements and upload of the necessary photos, we will ship the incentive gift to you with no shipping charge. Unless otherwise indicated, participation eligibility is restricted to US residents, 18 and over. Void where prohibited. <a href="#">Privacy Policy</a> | <a href="#">Unsubscribe</a></p>
  </footer>
</main>
</body>
</html>
```